Flyer Design Project

We need a flyer design for our company based in Ontario, Canada called CrateNest. We rent out plastic reusable moving boxes. Please visit Cratenest.ca to find out more information about our company. We are looking for a creative, clean, and fun flyer design. The flyers purpose is to share with others what services CrateNest offers as well as how convient our service is while still being cheaper than cardboard boxes.

Industry/Entity Type

Plastic

```html
<!DOCTYPE html>
<html lang="en">
<head>
<meta charset="utf-8">
<title>CrateNest – Plastic Moving Boxes Flyer</title>
<link rel="stylesheet" href="https://fonts.googleapis.com/css2?family=Arimo:wght@400;700&family=Roboto:wght@300&family=Oswald:wght@500&family=Archivo+Black&display=swap">
<style>
  :root {
    --surround: #4d4b4c;
    --paper: #ffffff;
    --ink: #1d1d1b;
    --muted: #6b6b6b;
    --brand-green: #7dc143;
    --deep-green: #3cb54a;
    --band-black: #1a1a1a;
  }
  * { margin: 0; padding: 0; box-sizing: border-box; }
  html, body { width: 953px; height: 1200px; overflow: hidden; background: var(--surround); }
  body { font-family: "Arimo", Arial, sans-serif; color: var(--ink); }

  .flyer {
    position: absolute; left: 43px; top: 42px;
    width: 863px; height: 1116px;
    background: radial-gradient(ellipse at 60% 40%, #ffffff 45%, #f1f1f1 100%);
    overflow: hidden;
  }

  .brand { position: absolute; left: 62px; top: 40px; display: flex; align-items: center; gap: 12px; }
  .brand-mark { width: 48px; height: 48px; background: var(--brand-green); border-radius: 8px; }
  .brand-name { font-family: "Arimo", Arial, sans-serif; font-weight: 700; font-size: 36px; color: var(--ink); letter-spacing: -0.5px; }

  .contact { position: absolute; right: 57px; top: 40px; text-align: right; }
  .contact-lead { font-weight: 700; font-size: 19px; color: var(--muted); }
  .contact-phone { display: flex; align-items: center; justify-content: flex-end; gap: 4px;
    font-weight: 700; font-size: 38px; color: var(--brand-green); margin-top: 4px; }
  .contact-phone svg { width: 20px; height: 30px; }

  .headline-kicker { position: absolute; left: 69px; top: 160px; font-weight: 700; font-size: 31px; color: var(--ink); }
  .headline-main { position: absolute; left: 66px; top: 196px; font-family: "Roboto", Arial, sans-serif;
    font-weight: 300; font-size: 94px; letter-spacing: -1px; color: var(--ink); line-height: 1.1; }

  .steps { position: absolute; left: 73px; top: 319px; width: 280px; list-style: none; }
  .step { margin-bottom: 12px; }
  .step-label { font-weight: 700; font-size: 14px; color: var(--muted); margin-bottom: 4px; }
  .step-row { display: flex; gap: 11px; }
  .step-icon { flex: none; width: 70px; height: 70px; background: var(--brand-green); border-radius: 9px;
    display: flex; align-items: center; justify-content: center; }
  .step-icon svg { width: 46px; height: 46px; }
  .step-text { font-weight: 700; font-size: 16px; line-height: 19px; color: var(--ink); margin-top: 1px; }

  .product-visual { position: absolute; left: 377px; top: 328px; width: 443px; height: 335px;
    background: linear-gradient(160deg, #a6d86a 0%, #86c64a 50%, #6aa636 100%);
    border-radius: 14px 14px 30px 30px; }

  .curve { position: absolute; left: 0; top: 0; width: 863px; height: 1116px; }

  .order-badge { position: absolute; left: 667px; top: 644px; width: 158px; height: 158px; border-radius: 50%;
    background: var(--paper); display: flex; align-items: center; justify-content: center; }
  .order-badge-inner { width: 144px; height: 144px; border-radius: 50%; background: var(--deep-green);
    display: flex; align-items: center; justify-content: center; text-align: center;
    font-family: "Oswald", Arial, sans-serif; font-weight: 500; font-size: 42px; line-height: 46px; color: #fff; }

  .reasons { position: absolute; left: 60px; top: 762px; width: 400px; color: #fff; }
  .reasons-title { font-family: "Archivo Black", Arial, sans-serif; font-size: 26px; }
  .reasons-sub { font-weight: 700; font-size: 23px; margin-top: 6px; }
  .reasons-body { font-weight: 700; font-size: 15px; line-height: 19.4px; margin-top: 12px; }

  .reason-list { position: absolute; left: 482px; top: 812px; list-style: none; }
  .reason { display: flex; align-items: center; gap: 16px; height: 30px; margin-bottom: 18px; }
  .reason-num { width: 30px; height: 30px; background: #fff; color: var(--brand-green);
    font-family: "Archivo Black", Arial, sans-serif; font-size: 24px; line-height: 30px; text-align: center; }
  .reason-text { font-family: "Oswald", Arial, sans-serif; font-weight: 500; font-size: 24px; color: #fff; }

  .web { position: absolute; right: 55px; top: 1075px; font-weight: 700; font-size: 19px; color: #fff; }
</style>
</head>
<body>
<main class="flyer">
  <div class="brand">
    <span class="brand-mark"></span>
    <span class="brand-name">CrateNest</span>
  </div>

  <div class="contact">
    <p class="contact-lead">Call us now with any questions</p>
    <p class="contact-phone">
      <svg viewBox="0 0 20 30" aria-hidden="true"><path d="M8 2 L3 4 Q0 15 3 26 L8 28 L10 22 L7 20 Q5 15 7 10 L10 8 Z" fill="#7dc143"/></svg>
      1-800-555-0142
    </p>
  </div>

  <h2 class="headline-kicker">Plastic, stackable, eco-friendly</h2>
  <h1 class="headline-main">moving boxes</h1>

  <ol class="steps">
    <li class="step">
      <p class="step-label">Step : 1</p>
      <div class="step-row">
        <span class="step-icon">
          <svg viewBox="0 0 46 46" aria-hidden="true"><rect x="3" y="12" width="24" height="18" fill="#fff"/><path d="M28 17 H36 L42 24 V30 H28 Z" fill="#fff"/><circle cx="11" cy="33" r="4" fill="#fff" stroke="#7dc143" stroke-width="2"/><circle cx="35" cy="33" r="4" fill="#fff" stroke="#7dc143" stroke-width="2"/></svg>
        </span>
        <p class="step-text">We deliver your moving boxes right to your front door (unless you prefer side door).</p>
      </div>
    </li>
    <li class="step">
      <p class="step-label">Step : 2</p>
      <div class="step-row">
        <span class="step-icon">
          <svg viewBox="0 0 46 46" aria-hidden="true"><path d="M9 20 L23 26 L37 20 V36 L23 42 L9 36 Z" fill="#fff"/><path d="M9 20 L3 12 L17 7 L23 14 L29 7 L43 12 L37 20 L23 14 Z" fill="#fff"/></svg>
        </span>
        <p class="step-text">Pack it up! Our boxes protect your belongings and make stacking safe.</p>
      </div>
    </li>
    <li class="step">
      <p class="step-label">Step : 3</p>
      <div class="step-row">
        <span class="step-icon">
          <svg viewBox="0 0 46 46" aria-hidden="true"><path d="M23 5 L42 22 H37 V41 H9 V22 H4 Z" fill="#fff"/><rect x="15" y="26" width="7" height="15" fill="#7dc143"/><rect x="26" y="26" width="6" height="6" fill="#7dc143"/></svg>
        </span>
        <p class="step-text">Once you're unpacked we'll come by your new home and collect the moving boxes.</p>
      </div>
    </li>
  </ol>

  <div class="product-visual" role="img" aria-label="Green plastic moving crate with hinged lid, shown in perspective"></div>

  <svg class="curve" viewBox="0 0 863 1116" aria-hidden="true">
    <path d="M0 628 Q330 712 863 706 L863 722 Q330 728 0 660 Z" fill="#1a1a1a"/>
    <path d="M0 654 Q330 726 863 716 L863 1116 L0 1116 Z" fill="#7dc143"/>
  </svg>

  <div class="order-badge"><div class="order-badge-inner">ORDER<br>NOW</div></div>

  <section class="reasons">
    <h2 class="reasons-title">Why choose CrateNest?</h2>
    <p class="reasons-sub">We have 5 good reasons</p>
    <p class="reasons-body">Packing boxes is the same no matter how old you are, what race you are, where you’re moving to, or what your favorite ice cream is. Packing is packing, but are boxes, boxes? We all remember the search for cardboard boxes from family, friends and even local grocery stores. We get a few good ones, a few mediocre ones and a few banana boxes with a big hole in the bottom. “That’s fine for bedding, right?”. But at the end of the day, we still didn’t have enough quality boxes. When you order from CrateNest, we have an answer for all the box problems we used to run into:</p>
  </section>

  <ol class="reason-list">
    <li class="reason"><span class="reason-num">1</span><span class="reason-text">WE DELIVER</span></li>
    <li class="reason"><span class="reason-num">2</span><span class="reason-text">PACK SECURELY</span></li>
    <li class="reason"><span class="reason-num">3</span><span class="reason-text">SAFELY STACK</span></li>
    <li class="reason"><span class="reason-num">4</span><span class="reason-text">WE PICKUP</span></li>
    <li class="reason"><span class="reason-num">5</span><span class="reason-text">ENVIRONMENTALLY FRIENDLY</span></li>
  </ol>

  <p class="web">www.cratenest.ca</p>
</main>
</body>
</html>
```